New business card design needed for Trucking/Staffing company!

I am looking for a business card design. The business name is Harbor Lane Freightworks, LLC. This company is a staffing company for commercial drivers/truck drivers. Most of our customers are trucking/supply companies. Our colors are blue/black/white/grey. The info I have on my current business cards is
-Spot for a name
-2 lines for an address
-3 lines for Office, cell, and fax
-email
-website(currently on backside of card with logo but can go anywhere)
Updates

Project Deadline Extended
Reason: Open to more designs

Target Market(s)

Trucking companies, building supply companies

Industry/Entity Type

Business

Contact Information for Business Card

Edgy but professional

Font styles to use
Other font styles liked:
• Open to suggestions

Colors
0555a3
000000
ffffff
9d9d9d

Requirements
Must have
• Must have the logo incorporated

```html
<!DOCTYPE html>
<html lang="en">
<head>
<meta charset="utf-8">
<title>Harbor Lane Freightworks, LLC – Business Card</title>
<link rel="stylesheet" href="https://fonts.googleapis.com/css2?family=Montserrat:wght@300;400;600;800&display=swap">
<style>
  :root {
    --brand-blue: #3049b6;
    --brand-blue-deep: #2437a0;
    --ink-black: #000000;
    --paper-white: #ffffff;
    --paper-grey: #ececec;
    --text-grey: #3a3a3a;
    --stage: #d9d9d9;
  }
  * { box-sizing: border-box; margin: 0; padding: 0; }
  html, body {
    width: 1200px; height: 780px; overflow: hidden;
    background: var(--stage);
    font-family: "Montserrat", sans-serif;
  }
  .sheet {
    position: relative; width: 1200px; height: 780px;
    display: flex; align-items: center; justify-content: center; gap: 40px;
  }
  .card {
    position: relative; width: 560px; height: 320px;
    border-radius: 18px; overflow: hidden;
    background: linear-gradient(160deg, var(--paper-white) 0%, var(--paper-grey) 100%);
    box-shadow: 0 10px 24px rgba(0,0,0,.25);
  }
  .card-bands { position: absolute; inset: 0; width: 100%; height: 100%; }
  .band-blue { fill: var(--brand-blue); }
  .band-black { fill: var(--ink-black); }

  .company-name {
    display: flex; align-items: center; gap: 10px;
    color: var(--brand-blue); font-weight: 800;
    text-transform: uppercase; letter-spacing: .5px; line-height: 1.1;
  }
  .company-name .mark-square {
    width: 14px; height: 14px; background: var(--brand-blue); flex: none;
  }

  /* Front */
  .card-front .company-name { position: absolute; left: 36px; top: 96px; font-size: 19px; }
  .card-front .address {
    position: absolute; left: 36px; top: 196px;
    font-size: 13px; font-weight: 400; color: var(--text-grey); line-height: 1.45;
  }
  .card-front .person {
    position: absolute; right: 36px; top: 26px; text-align: right;
  }
  .person-name { font-size: 17px; font-weight: 600; color: var(--brand-blue); letter-spacing: .5px; }
  .person-role { font-size: 13px; font-weight: 400; color: var(--text-grey); }
  .contact-list {
    position: absolute; right: 36px; top: 86px; list-style: none;
    font-size: 12.5px; color: var(--text-grey); line-height: 1.55;
  }
  .contact-list li { display: flex; align-items: center; justify-content: flex-end; gap: 8px; }
  .contact-icon {
    width: 15px; height: 15px; border-radius: 3px; background: var(--brand-blue);
    display: inline-flex; align-items: center; justify-content: center;
  }
  .contact-icon svg { width: 11px; height: 11px; fill: none; stroke: var(--paper-white); stroke-width: 1.6; }
  .website {
    position: absolute; color: var(--paper-white);
    font-size: 13px; font-weight: 400; letter-spacing: .3px;
  }
  .card-front .website { right: 36px; bottom: 26px; }

  /* Back */
  .card-back .company-name {
    position: absolute; left: 0; right: 0; top: 128px;
    justify-content: center; font-size: 24px;
  }
  .card-back .website { left: 0; right: 0; bottom: 24px; text-align: center; }
</style>
</head>
<body>
<main class="sheet">

  <section class="card card-front" aria-label="Business card front">
    <svg class="card-bands" viewBox="0 0 560 320" aria-hidden="true">
      <path class="band-black" d="M0,308 Q270,252 560,112 L560,146 Q300,262 30,320 L0,320 Z"/>
      <path class="band-blue" d="M70,320 Q320,262 560,158 L560,320 Z"/>
    </svg>

    <div class="company-name"><span class="mark-square"></span><span>Harbor Lane<br>Freightworks, LLC</span></div>

    <p class="address">PO Box 214 Harbor Lane<br>Bayport NY 11705</p>

    <div class="person">
      <p class="person-name">EMPLOYEE NAME</p>
      <p class="person-role">Owner</p>
    </div>

    <ul class="contact-list">
      <li>111-222-3333
        <span class="contact-icon"><svg viewBox="0 0 12 12"><path d="M3 1.5 L4.5 1.5 L5 4 L4 4.8 Q5 7 7.2 8 L8 7 L10.5 7.5 L10.5 9 Q10 10.5 8.5 10.5 Q2 9.5 1.5 3.5 Q1.5 2 3 1.5 Z"/></svg></span></li>
      <li>111-222-3333
        <span class="contact-icon"><svg viewBox="0 0 12 12"><rect x="3.5" y="1" width="5" height="10" rx="1"/><path d="M5.5 9.3 H6.5"/></svg></span></li>
      <li>111-222-3333
        <span class="contact-icon"><svg viewBox="0 0 12 12"><rect x="1.5" y="5" width="9" height="5" rx="1"/><path d="M3.5 5 V1.5 H8.5 V5"/></svg></span></li>
      <li>office@harborlanefreight.com
        <span class="contact-icon"><svg viewBox="0 0 12 12"><rect x="1.5" y="3" width="9" height="6.5"/><path d="M1.5 3 L6 7 L10.5 3"/></svg></span></li>
    </ul>

    <p class="website">www.harborlanefreight.com</p>
  </section>

  <section class="card card-back" aria-label="Business card back">
    <svg class="card-bands" viewBox="0 0 560 320" aria-hidden="true">
      <path class="band-blue" d="M0,0 H560 V26 Q300,60 0,92 Z"/>
      <path class="band-black" d="M0,104 Q300,70 560,36 L560,44 Q300,84 0,116 Z"/>
      <path class="band-black" d="M0,222 Q290,214 560,172 L560,196 Q290,232 0,238 Z"/>
      <path class="band-blue" d="M0,250 Q290,244 560,206 L560,320 H0 Z"/>
    </svg>

    <div class="company-name"><span class="mark-square"></span><span>Harbor Lane<br>Freightworks, LLC</span></div>

    <p class="website">www.harborlanefreight.com</p>
  </section>

</main>
</body>
</html>
```